International Legal Service Company needs Letterhead Design

Put my new Logo into Letterhead Design, using updated telephone number, e-mail address and website. Current letterhead and updated information which i want you to include my new letterhead attached herewith. Of course, my new Logo attached herein. Also, you can use slogan "Total Legal Outsourcing Solutions For Multinational Businesses"

It Company

```html
<!DOCTYPE html>
<html lang="en">
<head>
<meta charset="utf-8">
<title>Meridian Counsel Partners — Letterhead</title>
<link href="https://fonts.googleapis.com/css2?family=Montserrat:wght@300;600;700&family=Open+Sans:wght@400;600;700&display=swap" rel="stylesheet">
<style>
  :root {
    --paper: #ffffff;
    --navy: #1f3a78;
    --ink: #4a4a4a;
    --ink-dark: #333333;
    --muted: #7a7a7a;
    --rule: #1f3a78;
    --sig-tone: #f1f2f5;
  }
  * { margin: 0; padding: 0; box-sizing: border-box; }
  html, body { width: 942px; height: 1200px; overflow: hidden; background: var(--paper); }
  .letterhead {
    position: relative; width: 942px; height: 1200px; background: var(--paper);
    font-family: "Open Sans", Arial, sans-serif; color: var(--ink);
  }
  .brand-name {
    position: absolute; left: 74px; top: 76px;
    font-family: "Open Sans", Arial, sans-serif; font-weight: 600; font-size: 24px;
    line-height: 1; color: var(--navy); white-space: nowrap;
  }
  .meta { position: absolute; left: 125px; top: 258px; font-family: "Montserrat", Arial, sans-serif; font-size: 11px; line-height: 16px; color: var(--ink-dark); }
  .meta b { font-weight: 700; }
  .salutation { position: absolute; left: 125px; top: 312px; font-size: 12.4px; color: var(--ink); }
  .body-text { position: absolute; left: 125px; width: 734px; font-size: 12.4px; line-height: 25px; text-align: justify; color: var(--ink); }
  .p1 { top: 335px; } .p2 { top: 481px; } .p3 { top: 609px; }
  .signatory { position: absolute; left: 125px; top: 728px; }
  .signatory-name { font-family: "Montserrat", Arial, sans-serif; font-size: 23px; line-height: 1; color: var(--ink-dark); letter-spacing: .5px; }
  .signatory-name b { font-weight: 700; } .signatory-name span { font-weight: 300; }
  .signatory-role { font-family: "Montserrat", Arial, sans-serif; font-weight: 300; font-size: 12.5px; color: var(--muted); margin-top: 3px; }
  .signature { position: absolute; left: 123px; top: 798px; width: 255px; height: 120px; background: linear-gradient(120deg, var(--sig-tone), #fafbfc); border-radius: 6px; }
  .footer-rule { position: absolute; left: 0; top: 1061px; width: 282px; height: 2px; background: var(--rule); }
  .contact { position: absolute; left: 74px; top: 1076px; font-size: 11px; line-height: 18px; color: var(--muted); font-style: normal; }
  .contact b { color: var(--navy); font-weight: 700; }
  .contact .company { color: var(--navy); font-weight: 700; }
  .contact .company span { font-weight: 400; }
</style>
</head>
<body>
<main class="letterhead">
  <header class="brand-name">Meridian Counsel Partners Inc</header>

  <div class="meta">
    <div><b>Date :</b> Mon , 25 / 3 / 2013</div>
    <div><b>Recipient :</b> Mr. Alan Reed Whitford</div>
  </div>

  <p class="salutation">Dear Mr. Whitford</p>

  <p class="body-text p1">Lorem ipsum dolor sit amet, consectetur adipiscing elit. Praesent vulputate, neque ac accumsan suscipit, justo turpis volutpat nisl, tempus fermentum eros tortor et elit. Vivamus porttitor faucibus gravida. Quisque pharetra gravida luctus. Donec eget turpis libero. Ut ac dolor urna, quis tempor nunc. Donec vitae mauris purus, euismod eleifend nulla. Lorem ipsum dolor sit amet, consectetur adipiscing elit. Donec ut purus tellus. Aenean quis dignissim lacus. Vestibulum suscipit vehicula cursus. Suspendisse potenti. Ut in sem nisi. Sed et massa leo.</p>

  <p class="body-text p2">Fusce varius libero vel risus condimentum suscipit. Nullam tristique ultrices massa a volutpat. Donec sed dictum metus. Curabitur fringilla nibh eu ligula pharetra a interdum quam aliquam. Maecenas aliquam elit eu orci rutrum molestie. Proin nisl justo, varius a volutpat nec, ultricies sed sem. Nam sit amet imperdiet sem. Phasellus vitae mauris odio. Etiam in purus dui. Etiam ultricies, ante vel iaculis sodales, arcu leo adipiscing leo, sit amet mollis dui nisi non quam.</p>

  <p class="body-text p3">Suspendisse sagittis laoreet dolor, vitae rhoncus arcu volutpat quis. Vestibulum at placerat dolor. Vivamus eu lacus ut enim molestie consectetur. Quisque ac lorem vel orci sagittis sollicitudin. Nunc ut quam sem, quis volutpat libero. Cum sociis natoque penatibus et magnis dis parturient montes, nascetur ridiculus mus. Vestibulum ante ipsum primis in faucibus orci luctus et ultrices posuere cubilia Curae; Donec tempor velit in velit feugiat sit amet vulputate nisl posuere..</p>

  <div class="signatory">
    <div class="signatory-name"><b>DANIEL</b> <span>MARSH</span></div>
    <div class="signatory-role">General director</div>
  </div>

  <div class="signature" role="img" aria-label="Handwritten signature of the general director"></div>

  <div class="footer-rule"></div>
  <address class="contact">
    <div><b>P.</b> 555-204-7731 | <b>F.</b> 555-204-7790</div>
    <div class="company">MERIDIAN COUNSEL <span>PARTNERS INC</span></div>
    <div>1480 Harbor Point Avenue, Suite 300</div>
    <div>Lakemont, VA 22190</div>
    <div><b>E.</b> contact@meridiancounsel.com</div>
    <div><b>W.</b> www.meridiancounsel.com</div>
  </address>
</main>
</body>
</html>
```